Designing promotion page - poster for Folk High School

I would like a attractive and well-designed page /poster used in a catalogue for the Norwegian Folk High Schools.
The dimensions on the graphical element:
Width: 180 mm
Hight:186 mm
Resolution: min. 450 dpi
This graphical element will be combined with other information about the school, that is static and we cannot change. Please see attachment (“Folk High School – placement of graphic”). The almost square area in the middle of the page iss the one that the designed grapichal element will fill.
A part of completing this, is to hand over the workfile to us in the end when we choose the design (Adobe Photoshop PSD or an InDesign INDD file must be used)
There are also attached some pictures that you are free to use in creating the design as you like. You will choose how many pictures you want to use. Please cut, scale, adjust and sharpen them as you like. Only one requirement: Please use one of the Sri Lanka pictures.
Be creative.
The following text-elements must be used in the page (They are also prioritized – number one means: most important that the reader reads…)
1. Møtet som forandrer --- headline. Yep; needs a font supporting ÆØÅ...
2. Multisport --- different courses we provide at our school.
- Data Media – Japan
- Barn i Fokus
- Helse og Velvære
- Globalt Fokus – Afrika
- Fotball
- Bil og Motor
- Internasjonal
- Worship – Australia
- LYNG-friluft
- Høy Puls
Alle linjer reiser på egne turer i inn –og utland! ---- This should be included as the different courses, but in the bottum of the «box».
3. Spennende fellestur for alle til Sri Lanka ---- Use together with the picture from Sri Lanke (Not too large picture!)
4. Hva skal du bli? ---- small headline.
Vi er gode på veiledning, og hjelper deg med å finne ut hva du skal bli.
5. Flott skole:
- Basseng
- Styrkerom
- Gymsal
- Internatstuer
- Filmsal
- Skolekjøkken
- Verksted
- Fotostudio
- Fitnessrom
_________
The students attending our school is between 18-20 years. Of course, the design and expression must meet their expectations.
Looking forward to see the first drafts!
To understand what this should look like: Check the following link:
https://pagevault.example/trondelsk/docs/trk_hefte__18__web
The poster / graphic we want to create, is similar to the one you find in this brochure from page 20.

```html
<!DOCTYPE html>
<html lang="no">
<head>
<meta charset="utf-8">
<title>Møtet som forandrer – Lyngvik Folkehøgskule</title>
<link rel="stylesheet" href="https://fonts.googleapis.com/css2?family=Arimo:wght@400;700&display=swap">
<style>
  :root {
    --bg: #ececec;
    --paper: #ffffff;
    --ink: #1c1c1c;
    --ink-soft: #3a3a3a;
    --rule: #2a2a2a;
    --sky-top: #7fb3e6;
    --sky-bottom: #e4eef8;
    --sea-top: #4f86c9;
    --sea-bottom: #c9b79a;
    --beach-top: #6aa6d8;
    --beach-bottom: #d9be86;
  }
  html, body {
    margin: 0;
    width: 1200px;
    height: 1200px;
    overflow: hidden;
    background: var(--bg);
    font-family: "Arimo", Arial, sans-serif;
    color: var(--ink);
  }
  .page {
    position: absolute;
    left: 225px;
    top: 20px;
    width: 750px;
    height: 1160px;
    background: var(--paper);
  }
  .page > * { position: absolute; margin: 0; }

  .school-name { left: 45px; top: 42px; font-size: 28px; font-weight: 700; letter-spacing: -0.3px; }
  .school-facts { left: 47px; top: 83px; font-size: 13.5px; line-height: 19.2px; color: var(--ink-soft); list-style: none; padding: 0; }
  .header-divider { left: 533px; top: 34px; width: 2px; height: 148px; background: var(--rule); }
  .logo-note { left: 560px; top: 52px; width: 150px; text-align: center; font-size: 20px; line-height: 27px; }
  .web-link { left: 560px; top: 182px; width: 150px; text-align: center; font-size: 13px; }

  .rule-h { left: 51px; width: 652px; height: 2.5px; background: var(--rule); }
  .rule-top { top: 213px; }
  .rule-bottom { top: 1007px; }

  .photo { display: block; }
  .photo-jump { left: 51px; top: 232px; width: 384px; height: 187px; background: linear-gradient(180deg, var(--sky-top), var(--sky-bottom)); }
  .photo-friends { left: 196px; top: 452px; width: 347px; height: 257px; background: linear-gradient(180deg, var(--sea-top), var(--sea-bottom)); }
  .photo-beach { left: 51px; top: 797px; width: 308px; height: 195px; background: linear-gradient(180deg, var(--beach-top) 0%, #a9cde6 45%, var(--beach-bottom) 62%); }

  .headline { font-weight: 700; letter-spacing: -2px; line-height: 1; z-index: 2; }
  .headline-motet { left: 463px; top: 238px; font-size: 96px; }
  .headline-som { left: 45px; top: 432px; font-size: 76px; }
  .headline-forandrer { left: 303px; top: 730px; font-size: 96px; }

  .course-title { left: 571px; top: 377px; font-size: 27px; }
  .course-list { left: 572px; top: 421px; list-style: none; padding: 0; font-size: 14px; line-height: 21.2px; }

  .trip-note { left: 51px; top: 738px; font-size: 15px; line-height: 20px; }
  .guidance { left: 500px; top: 900px; font-size: 15px; line-height: 20px; }

  .facilities-title { left: 51px; top: 1033px; font-size: 18px; }
  .facility-col { top: 1063px; list-style: none; padding: 0; font-size: 13.5px; line-height: 19px; }
  .facility-col-1 { left: 51px; }
  .facility-col-2 { left: 144px; }
  .facility-col-3 { left: 254px; }
  .footer-divider { left: 466px; top: 1030px; width: 2px; height: 93px; background: var(--rule); }
  .travel-note { left: 483px; top: 1040px; font-size: 19px; line-height: 26px; font-weight: 700; }
</style>
</head>
<body>
<main class="page">
  <h1 class="school-name">LYNGVIK FOLKEHØGSKULE</h1>
  <ul class="school-facts">
    <li>Adresse : Lyngvikvegen 12, 6999 Lyngvik</li>
    <li>Telefon : 70 00 00 00</li>
    <li>E-post : kontor@lyngvik.example</li>
    <li>Elevplasser : 90</li>
    <li>Aldersgrense : 18 år</li>
    <li>Eigar : Lyngvik-stiftinga</li>
  </ul>
  <div class="header-divider"></div>
  <p class="logo-note">*provide<br>logo<br>please*</p>
  <p class="web-link">lv.hefte.example</p>

  <div class="rule-h rule-top"></div>

  <div class="photo photo-jump" role="img" aria-label="Fire elever som hopper mot en blå himmel med skyer"></div>
  <h2 class="headline headline-motet">Møtet</h2>

  <p class="course-title">Multisport</p>
  <ul class="course-list">
    <li>Data Media – Japan</li>
    <li>Barn i Fokus</li>
    <li>Helse og Velvære</li>
    <li>Globalt Fokus – Afrika</li>
    <li>Fotball</li>
    <li>Bil og Motor</li>
    <li>Internasjonal</li>
    <li>Worship – Australia</li>
    <li>LYNG-friluft</li>
    <li>Høy Puls</li>
  </ul>

  <div class="photo photo-friends" role="img" aria-label="To venninner med solbriller på en strand ved havet"></div>
  <h2 class="headline headline-som">som</h2>

  <p class="trip-note">Spennende fellestur<br>for alle til Sri Lanka</p>
  <div class="photo photo-beach" role="img" aria-label="Sandstrand med palmer og bølger på Sri Lanka"></div>
  <h2 class="headline headline-forandrer">forandrer</h2>

  <p class="guidance">Hva skal du bli?<br>Vi er gode på veiledning,<br>og hjelper deg med å finne<br>ut hva du skal bli.</p>

  <div class="rule-h rule-bottom"></div>

  <p class="facilities-title">Flott skole :</p>
  <ul class="facility-col facility-col-1"><li>Basseng</li><li>Styrkerom</li><li>Gymsal</li></ul>
  <ul class="facility-col facility-col-2"><li>Internatstuer</li><li>Filmsal</li><li>Skolekjøkken</li></ul>
  <ul class="facility-col facility-col-3"><li>Verksted</li><li>Fotostudio</li><li>Fitnessrom</li></ul>
  <div class="footer-divider"></div>
  <p class="travel-note">Alle linjer reiser på egne<br>turer i inn –og utland!</p>
</main>
</body>
</html>
```